Business Card Design for a Handbags business

We are modernising our handbags website (see attached file for new front page) and are in need of a modern business card and a related design we can use on a small marquee at the markets, on letterhead, emails etc.

As the leather handbags we mostly import are from Italy, we want a smart modern European feel to the design. We are currently thinking about changing the name of the business from Larkmoor Handbags (see www.larkmoorhandbags.com.au) to Vintessa Handbags. Also open to other suggestions you may have that communicates the European influence and quality.

Target Market(s)

25-65 year old women (and some men)

Industry/Entity Type

Business

Contact Information for Business Card

Single or double sided - whichever creates more of an impact

Font styles to use
Serif
Sans Serif

Requirements
Must have
• Clean crisp look, slightly Italian or European look and feel to reflect where the handbags are imported from
Nice to have
• open to ideas

```html
<!DOCTYPE html>
<html lang="en">
<head>
<meta charset="utf-8">
<title>Business Card – Luxury Leather Handbags</title>
<link rel="stylesheet" href="https://fonts.googleapis.com/css2?family=Open+Sans:wght@400;600;700&family=Tinos&display=swap">
<style>
  :root {
    --backdrop: #8c8178;
    --card-white: #ffffff;
    --cream-light: #f4ede0;
    --cream-mid: #e6dccb;
    --cream-deep: #d8ccb8;
    --band-taupe: #938a7c;
    --ink: #141414;
    --shadow: rgba(40, 30, 20, 0.35);
  }
  * { margin: 0; padding: 0; box-sizing: border-box; }
  html, body {
    width: 1200px;
    height: 864px;
    overflow: hidden;
    background: var(--backdrop);
  }
  .canvas {
    width: 1200px;
    height: 864px;
    display: flex;
    align-items: center;
    justify-content: center;
    gap: 60px;
  }
  .card {
    width: 520px;
    height: 318px;
    position: relative;
    overflow: hidden;
    box-shadow: 0 10px 26px var(--shadow);
  }

  /* Back: name side */
  .card--name {
    background: var(--card-white);
    display: flex;
    align-items: center;
    justify-content: center;
  }
  .person-name {
    font-family: "Open Sans", Arial, sans-serif;
    font-weight: 400;
    font-size: 30px;
    letter-spacing: 4px;
    line-height: 1.2;
    color: var(--ink);
    text-align: center;
  }

  /* Front: brand side */
  .card--brand { background: var(--cream-light); }
  .product-photo {
    position: absolute;
    left: 0;
    width: 100%;
  }
  .product-photo--top {
    top: 0;
    height: 118px;
    background: linear-gradient(180deg, var(--cream-deep) 0%, var(--cream-light) 100%);
  }
  .product-photo--bottom {
    bottom: 0;
    height: 96px;
    background: linear-gradient(180deg, var(--cream-light) 0%, var(--cream-mid) 100%);
  }
  .tagline-band {
    position: absolute;
    left: 0;
    top: 118px;
    width: 100%;
    height: 104px;
    background: var(--band-taupe);
    display: flex;
    align-items: center;
    justify-content: flex-end;
    padding-right: 26px;
  }
  .tagline {
    font-family: "Tinos", "Times New Roman", serif;
    font-size: 40px;
    color: var(--ink);
    white-space: nowrap;
  }
  .phone {
    position: absolute;
    left: 150px;
    top: 240px;
    display: flex;
    align-items: center;
    gap: 8px;
    font-family: "Open Sans", Arial, sans-serif;
    font-weight: 700;
    font-size: 19px;
    color: var(--ink);
  }
  .phone-icon { width: 18px; height: 18px; fill: var(--ink); }
</style>
</head>
<body>
  <main class="canvas">
    <section class="card card--name">
      <p class="person-name">Clara<br>Westwood</p>
    </section>

    <section class="card card--brand">
      <div class="product-photo product-photo--top" role="img" aria-label="Photograph of a row of coloured leather handbags"></div>
      <div class="tagline-band">
        <h1 class="tagline">Luxury Leather Handbags</h1>
      </div>
      <div class="product-photo product-photo--bottom" role="img" aria-label="Photograph of leather handbags viewed from above"></div>
      <p class="phone">
        <svg class="phone-icon" viewBox="0 0 24 24" aria-hidden="true">
          <path d="M3 8c0-2 3-4 9-4s9 2 9 4v2h-5V8.5c-1-.6-2.5-.9-4-.9s-3 .3-4 .9V10H3z"/>
          <path d="M6 12l2-3h8l2 3v7H6z M12 13a2.5 2.5 0 1 0 0 5a2.5 2.5 0 0 0 0-5z"/>
        </svg>
        0400 555 019
      </p>
    </section>
  </main>
</body>
</html>
```